Website for Public Relations Agency called "Tall Pine"

A need a website for a new business which is essentially a Public Relations/ Marketing business. We offer services to small family businesses, medium enterprise as well as multinational companies (ie we sell our professional services to other businesses; we are not a consumer brand).
The website needs to be polished, professional and modern. Because of the services we offer, I really need the website to be a little bit "wow".
Colours - we have a logo (see files) so the colour palette for the website should be dictated by this.
The Word doc attached mapped out the various pages that will make up the site. The text is not 100% finalised but it's good enough to give you a good picture of what the site will talk about.
I am not selling directly off my site, so this is an informational site only to explain who i am and what i do.
Target Market(s)
Other businesses - small family business, medium business and large multinational companies
Industry/Entity Type
Marketing
Coding
Coded - Design and coding required
Number of Pages Required
5+ page
Requirements
Must have
- Given my business, really looking for a little "wow" factor on the home page
Should not have
- I don't know if this is relevant to the coding, but I want to end up on a platform that I can myself make copy/ text edits as I please. I do not want to have to go through a deisgn company for small text changes in 6 or 12 months time.

```html
<!DOCTYPE html>
<html lang="en">
<head>
<meta charset="utf-8">
<title>Tall Pine – Strategic Communication</title>
<link href="https://fonts.googleapis.com/css2?family=Outfit:wght@300;400;500;600;700&display=swap" rel="stylesheet">
<style>
:root{
  --navy:#2b2562;
  --navy-deep:#241f55;
  --pink:#e0509e;
  --pink-soft:#e96fb0;
  --mauve:#9b83bd;
  --white:#ffffff;
  --ink:#2b2562;
  --muted:#8b84b0;
  --rule:#dcd8e8;
}
*{box-sizing:border-box;margin:0;padding:0}
html,body{width:1200px;height:2944px;overflow:hidden}
body{position:relative;font-family:'Outfit',sans-serif;color:var(--ink);background:var(--white)}
.abs{position:absolute}
a{color:inherit;text-decoration:none}
.btn{position:absolute;display:flex;align-items:center;justify-content:center;font-size:10px;font-weight:600;border-radius:4px}
.btn-mauve{background:var(--mauve);color:var(--white)}
.btn-pink{background:var(--pink);color:var(--white)}
.btn-white{background:var(--white);color:var(--navy)}

/* header + hero */
.hero-band{left:0;top:0;width:1200px;height:550px;background:var(--navy)}
.hero-photo{left:381px;top:75px;width:819px;height:550px;background:linear-gradient(120deg,#a9b7a8 0%,#d6c9bb 45%,#8a8f86 75%,#cfc5b8 100%)}
.brand{left:75px;top:26px;font-size:32px;font-weight:500;color:var(--pink);display:flex;align-items:center;gap:10px}
.brand-dot{width:14px;height:14px;background:var(--pink);border-radius:50%}
.nav{left:631px;top:31px;display:flex;gap:0;font-size:10px;color:var(--white)}
.nav a{position:absolute;white-space:nowrap}
.nav .active{color:var(--pink)}
.nav-phone{left:871px;top:29px;display:flex;align-items:center;gap:8px;font-size:11px;color:var(--white)}
.hero-kicker{left:75px;top:194px;font-size:15px;color:var(--pink)}
.hero-title{left:75px;top:227px;font-size:31px;font-weight:700;line-height:35px;color:var(--white);width:620px}
.hero-text{left:75px;top:313px;font-size:12.5px;line-height:19px;color:var(--white);width:520px}

/* messaging */
.collage{left:106px;top:625px;width:275px;height:358px;border-radius:6px;background:linear-gradient(160deg,#c94e95 0%,#8a3c7a 55%,#5a3a6f 100%)}
.msg-title{left:470px;top:718px;font-size:31px;line-height:35px;font-weight:400;color:var(--navy)}
.msg-title b{color:var(--pink);font-weight:600}
.msg-list{left:470px;top:816px;width:520px;list-style:none;font-size:9.5px;font-weight:500;color:var(--navy)}
.msg-list li{position:relative;padding-left:18px;line-height:15px;margin-bottom:10px}
.msg-list li svg{position:absolute;left:0;top:3px}

/* get in touch band */
.cta-band{left:0;top:1057px;width:1200px;height:344px;background:radial-gradient(ellipse at 30% 40%,#342d70 0%,var(--navy-deep) 70%)}
.cta-kicker{left:0;top:1132px;width:1200px;text-align:center;font-size:20px;font-weight:500;color:var(--pink)}
.cta-title{left:0;top:1165px;width:1200px;text-align:center;font-size:25px;font-weight:500;line-height:30px;color:var(--white)}

/* services */
.services{left:0;top:1401px;width:1200px;height:569px;background:linear-gradient(90deg,#e05aa3 0%,#e16aac 45%,#c98ab8 75%,#b9a0c0 100%)}
.svc-title{left:200px;top:1476px;font-size:30px;line-height:35px;color:var(--navy);font-weight:400}
.svc-title b{font-weight:600}
.svc-list{left:200px;top:1571px;list-style:none;font-size:12px;font-weight:500;color:var(--white);width:440px}
.svc-list li{position:relative;padding-left:18px;line-height:22.5px;margin-bottom:2.5px}
.svc-list li::before{content:"";position:absolute;left:0;top:7px;width:8px;height:8px;border:1.5px solid var(--mauve);border-radius:2px}

/* testimonials */
.divider-v{left:406px;top:2046px;width:1px;height:445px;background:var(--rule)}
.t-title{left:133px;top:2233px;font-size:30px;line-height:35px;color:var(--navy);font-weight:400}
.t-title b{font-weight:600}
.quote{left:512px;top:2047px;width:616px;font-size:11.3px;line-height:21.3px;color:var(--muted)}
.quote p{margin-bottom:21px}
.t-name{left:512px;top:2301px;font-size:14px;color:var(--navy);font-weight:500}
.t-org{left:512px;top:2322px;font-size:11px;color:var(--muted)}
.divider-h{left:512px;top:2366px;width:614px;height:1px;background:var(--rule)}
.avatar{border-radius:50%;background:linear-gradient(160deg,#e7e3ee,#c9c3d3)}

/* footer */
.footer{left:0;top:2575px;width:1200px;height:369px;background:var(--navy)}
.f-brand{left:200px;top:2669px;font-size:38px;font-weight:500;color:var(--pink);display:flex;align-items:center;gap:12px}
.f-social{left:291px;top:2785px;width:37px;height:37px;border:1px solid var(--mauve);border-radius:50%}
.f-head{font-size:14px;font-weight:500;color:var(--white)}
.f-line{display:flex;align-items:center;gap:10px;font-size:13px;color:var(--mauve)}
.f-text{left:782px;top:2712px;width:200px;font-size:12px;line-height:17px;color:var(--mauve)}
.f-input{left:782px;top:2785px;width:218px;height:37px;border-radius:4px;background:#3a3275;display:flex;align-items:center;justify-content:space-between;padding:0 14px;font-size:9px;color:var(--white)}
.f-bottom{top:2902px;font-size:10px;color:var(--mauve)}
.f-bottom b{color:var(--pink);font-weight:500}
.f-links{left:493px;top:2902px;display:flex;gap:12px;font-size:10px;color:var(--mauve)}
.f-links .active{color:var(--pink)}
</style>
</head>
<body>

<!-- header + hero -->
<div class="abs hero-band"></div>
<div class="abs hero-photo" role="img" aria-label="Photo of a smiling businesswoman seated at a laptop in a bright office"></div>

<div class="abs brand"><span class="brand-dot"></span>Tall Pine</div>

<nav class="abs nav" style="left:0;top:31px;width:1200px;height:14px">
  <a class="active" style="left:631px">Home</a>
  <a style="left:682px">About</a>
  <a style="left:735px">How we help</a>
  <a style="left:818px">Fees</a>
</nav>
<div class="abs nav-phone">
  <svg width="12" height="12" viewBox="0 0 24 24" fill="none" stroke="#e0509e" stroke-width="2"><path d="M22 16.9v3a2 2 0 0 1-2.2 2 19.8 19.8 0 0 1-8.6-3.1 19.5 19.5 0 0 1-6-6A19.8 19.8 0 0 1 2.1 4.2 2 2 0 0 1 4.1 2h3a2 2 0 0 1 2 1.7c.1.9.4 1.8.7 2.7a2 2 0 0 1-.5 2.1L8 9.8a16 16 0 0 0 6 6l1.3-1.3a2 2 0 0 1 2.1-.4c.9.3 1.8.6 2.7.7a2 2 0 0 1 1.7 2z"/></svg>
  +61 411 538 270
</div>
<a class="btn btn-pink" style="left:1013px;top:18px;width:112px;height:37px">Get in touch</a>

<div class="abs hero-kicker">Carefully Considered. Expertly Crafted.</div>
<h1 class="abs hero-title">Strategic Communication &amp; Reputation Management Specialist</h1>
<p class="abs hero-text">When you have a message to deliver, a story to tell, something to say that you need your stakeholders to hear loud and clear... Tall Pine can help.</p>
<a class="btn btn-mauve" style="left:75px;top:375px;width:125px;height:36px">Contact us today!</a>

<!-- messaging -->
<div class="abs collage" role="img" aria-label="Collage of team meeting photos in pink tones"></div>
<h2 class="abs msg-title">In Business, <b>Messaging<br>Always Matters</b></h2>
<ul class="abs msg-list">
  <li><svg width="10" height="8" viewBox="0 0 10 8" fill="none" stroke="#e0509e" stroke-width="1.2"><path d="M0 4h9M6 1l3 3-3 3"/></svg>Do you have a message to share that will build trust with the audiences that drive your revenue?</li>
  <li><svg width="10" height="8" viewBox="0 0 10 8" fill="none" stroke="#e0509e" stroke-width="1.2"><path d="M0 4h9M6 1l3 3-3 3"/></svg>Perhaps you need help promoting your people or services, or ensure they are known by a wider audience?</li>
  <li><svg width="10" height="8" viewBox="0 0 10 8" fill="none" stroke="#e0509e" stroke-width="1.2"><path d="M0 4h9M6 1l3 3-3 3"/></svg>Is there a narrative to be carefully devised and managed to prevent the erosion of trust amongst your important stakeholders, either internal or external?</li>
  <li><svg width="10" height="8" viewBox="0 0 10 8" fill="none" stroke="#e0509e" stroke-width="1.2"><path d="M0 4h9M6 1l3 3-3 3"/></svg>Do you have a situation on your hands, and you feel like you need to go into damage control?</li>
  <li><svg width="10" height="8" viewBox="0 0 10 8" fill="none" stroke="#e0509e" stroke-width="1.2"><path d="M0 4h9M6 1l3 3-3 3"/></svg>Has the media come knocking and you're not sure what to say?</li>
  <li><svg width="10" height="8" viewBox="0 0 10 8" fill="none" stroke="#e0509e" stroke-width="1.2"><path d="M0 4h9M6 1l3 3-3 3"/></svg>Do you need a website that is cohesive and sharp?</li>
</ul>

<!-- get in touch band -->
<div class="abs cta-band"></div>
<div class="abs cta-kicker">Get in touch</div>
<h2 class="abs cta-title">We'd love to talk about how we can help shape your narrative,<br>overcome your communications challenges, and<br>support you to say what needs to be said.</h2>
<a class="btn btn-pink" style="left:538px;top:1286px;width:124px;height:36px">Contact us today!</a>

<!-- services -->
<div class="abs services" role="img" aria-label="Photo of colleagues working together at a laptop, tinted pink"></div>
<h2 class="abs svc-title">We Help You <b>Communicate with<br>Clarity &amp; Impact</b></h2>
<ul class="abs svc-list">
  <li>Media Strategy, Liaison, Management And Execution</li>
  <li>Crisis, Issues &amp; Reputation Management (Specialising In Post Cyber Incident Communications)</li>
  <li>Corporate Communication</li>
  <li>Executive &amp; Internal Communication</li>
  <li>Communications Strategy &amp; Counsel</li>
  <li>B2B Public Relations</li>
  <li>Brand Building</li>
  <li>Copyrighting (In All Its Forms)</li>
  <li>Narrative Development</li>
  <li>Change Communications</li>
</ul>
<a class="btn btn-white" style="left:200px;top:1857px;width:112px;height:37px">Get in touch</a>

<!-- testimonials -->
<div class="abs divider-v"></div>
<h2 class="abs t-title">What clients<br><b>think about us</b></h2>
<a class="btn btn-mauve" style="left:133px;top:2328px;width:124px;height:37px">Contact us today!</a>

<div class="abs quote">
  <p>"We engaged Clara Whitmore of Tall Pine to assist with an announcement about leadership changes and growth ambitions. Crafting the right message for our market was a challenge; strategically we were hoping for some industry media coverage. Clara did what Clara said she would and successfully secured this coverage to meet our objectives.</p>
  <p>Clara made the entire process quick and seamless. She took the time to ask insightful questions to truly understand the message we wanted to convey. The end result was exactly what we needed. Our press release was picked up by the targeted publications, and the response from the market was overwhelmingly positive.</p>
  <p>We are extremely impressed with Clara's media counsel and highly recommend Tall Pine to anyone in need of professional, impactful media relations services and/or great copywriting."</p>
</div>
<div class="abs t-name">Marcus Delaney</div>
<div class="abs t-org">Harbour Ridge Insurance</div>
<div class="abs divider-h"></div>

<svg class="abs" style="left:512px;top:2424px" width="22" height="10" viewBox="0 0 22 10" fill="none" stroke="#e0509e" stroke-width="1.3"><path d="M22 5H1M5 1L1 5l4 4"/></svg>
<div class="abs avatar" style="left:556px;top:2404px;width:50px;height:50px" role="img" aria-label="Client portrait"></div>
<div class="abs avatar" style="left:668px;top:2404px;width:50px;height:50px" role="img" aria-label="Client portrait"></div>
<div class="abs avatar" style="left:781px;top:2392px;width:75px;height:75px;background:linear-gradient(160deg,#d9d3e2,#a79fb6)" role="img" aria-label="Portrait of the featured client"></div>
<div class="abs avatar" style="left:918px;top:2404px;width:50px;height:50px" role="img" aria-label="Client portrait"></div>
<div class="abs avatar" style="left:1031px;top:2404px;width:50px;height:50px" role="img" aria-label="Client portrait"></div>
<svg class="abs" style="left:1104px;top:2424px" width="22" height="10" viewBox="0 0 22 10" fill="none" stroke="#e0509e" stroke-width="1.3"><path d="M0 5h21M17 1l4 4-4 4"/></svg>

<!-- footer -->
<footer class="abs footer"></footer>
<div class="abs f-brand"><span class="brand-dot" style="width:16px;height:16px"></span>Tall Pine</div>
<div class="abs f-social" aria-label="Social profile"></div>

<div class="abs f-head" style="left:493px;top:2680px">Contact Us</div>
<div class="abs f-line" style="left:493px;top:2715px">
  <svg width="12" height="12" viewBox="0 0 24 24" fill="none" stroke="#e0509e" stroke-width="2"><path d="M22 16.9v3a2 2 0 0 1-2.2 2 19.8 19.8 0 0 1-8.6-3.1 19.5 19.5 0 0 1-6-6A19.8 19.8 0 0 1 2.1 4.2 2 2 0 0 1 4.1 2h3a2 2 0 0 1 2 1.7c.1.9.4 1.8.7 2.7a2 2 0 0 1-.5 2.1L8 9.8a16 16 0 0 0 6 6l1.3-1.3a2 2 0 0 1 2.1-.4c.9.3 1.8.6 2.7.7a2 2 0 0 1 1.7 2z"/></svg>
  +61 411 538 270
</div>
<div class="abs f-line" style="left:493px;top:2745px">
  <svg width="12" height="12" viewBox="0 0 24 24" fill="#e0509e"><path d="M2 9l10-6 10 6v11H2z"/></svg>
  clara.whitmore@tallpine.com.au
</div>
<a class="btn btn-pink" style="left:493px;top:2785px;width:112px;height:37px">Get in touch</a>

<div class="abs f-head" style="left:782px;top:2680px">Stay Connected</div>
<p class="abs f-text">Sign up for newsletter to receive Upadates, tips, and exclusive content.</p>
<div class="abs f-input">Enter your email...
  <svg width="12" height="10" viewBox="0 0 12 10" fill="#e0509e"><path d="M0 0l12 5-12 5 2-5z"/></svg>
</div>

<div class="abs f-bottom" style="left:200px">© 2024 <b>Tall Pine</b>. All Rights Reserved</div>
<div class="abs f-links"><span class="active">Home</span><span>|</span><span>About</span><span>|</span><span>How we help</span><span>|</span><span>Fees</span></div>
<svg class="abs" style="left:1117px;top:2898px" width="16" height="17" viewBox="0 0 16 17" fill="#e0509e"><path d="M8 0l8 17-8-5-8 5z"/></svg>

</body>
</html>
```